Newly created Management Consulting company needs a brochure to capture clients's interest

This is a new management consulting firm providing service in Finance, Marketing, Operations/Manufacturing Strategy, and Project Management.
Please go to the company's website: www.talvenbridgeadvisory.ca . The website is pretty straightforward and gives a clear explanation of all the services and sub-services offered. Based on the existent material on the website, I would like to create a company's brochure that can inspire clients to seek our services.
One important thing: the slogan/tagline ("Shaping the future of your business") needs to be added somewhere in the vicinity of our company's' LOGO. Please see attached the company's logo (JPEG file).
The brochure size and number of pages can vary, depending on the layout of the brochure so it can fit the content, so I am open to different and innovative sizes/shapes and no. of pages etc. Graphics should combine real pictures with graphic design technology, and should give a professional look and feel comparable to big companies' marketing materials.
Updates
The brochure does not necessarily have to include pictures that are on the website. If you think that other pictures and graphics can deliver a stronger message to customers, by all means I am open to any other ideas.
Thanks.
As I said before, the pictures do not need to be exactly the same pictures as on the website, if you can bring in other cool pictures to attract clients, please go ahead. Also, you do not need to use only black background, if you have better colors ideas to combine with the our LOGO, and it looks good, by all means do use other colors. But our LOGO needs to be represented as it is on the JPEG I attached.
May the most creative and cool design win! Good luck!
Please ensure that all the content of our website fits into your brochure, including our contact information. It is up to you to come up with the necessary number of pages, design and shape of the brochure, but the text should be clear enough to be read by a normal person without a magnifying glass.
Thank you.
In order to keep the brochure to a reasonable number of pages, I agree that it is not necessary to include 100% all the text that appears on the website. That being said, even if you do not have enough space to include all the background and introduction paragraphs under each service/sub-service, it is still important that the main message for each service/sub-service is being contained in the brochure.
Target Market(s)
Our clients are companies with sizes starting from 10-20 employees and up to large Corvane 300 companies.
Industry/Entity Type
Management Consulting
Look and feel

```html
<!DOCTYPE html>
<html lang="en">
<head>
<meta charset="utf-8">
<title>Talvenbridge Advisory – Marketing Spread</title>
<link href="https://fonts.googleapis.com/css2?family=Open+Sans:wght@300;400;600;700&display=swap" rel="stylesheet">
<style>
  :root {
    --stage: #e9e9e9;
    --page: #f4f4f4;
    --page-shade: #e2e2e2;
    --green: #5d9e2f;
    --green-dark: #4a8a22;
    --lime: #a8cf38;
    --ink: #1a1a1a;
    --text: #555555;
    --rule: #b9b9b9;
    --footer: #111111;
    --footer-text: #8a8a8a;
    --white: #ffffff;
  }
  * { margin: 0; padding: 0; box-sizing: border-box; }
  html, body { width: 1200px; height: 793px; overflow: hidden; }
  body {
    background: var(--stage);
    font-family: "Open Sans", Arial, sans-serif;
    position: relative;
  }
  .spread {
    position: absolute; left: 40px; top: 116px;
    width: 1120px; height: 560px;
    display: flex;
    box-shadow: 0 6px 18px rgba(0,0,0,.25);
  }
  .page { position: relative; width: 560px; height: 560px; overflow: hidden; }
  .page--left { background: linear-gradient(90deg, var(--page-shade) 0%, var(--page) 12%, var(--page) 88%, #dcdcdc 100%); }
  .page--right { background: linear-gradient(90deg, #d8d8d8 0%, var(--page) 10%, var(--page) 100%); }

  .top-band {
    position: absolute; left: 0; top: 0; width: 100%; height: 18px;
    background: linear-gradient(180deg, var(--lime), var(--green));
  }
  .page-footer {
    position: absolute; left: 0; bottom: 0; width: 100%; height: 22px;
    background: var(--footer);
  }
  .site-address {
    position: absolute; left: 38px; top: 4px;
    font-size: 10px; color: var(--footer-text); letter-spacing: .2px;
  }

  .services {
    position: absolute; left: 104px; top: 63px;
    width: 340px;
    display: grid;
    grid-template-columns: 168px 168px;
    grid-template-rows: 213px 213px;
    column-gap: 4px; row-gap: 11px;
  }
  .service {
    position: relative;
    border-right: 1px dashed var(--rule);
    border-bottom: 1px dashed var(--rule);
    border-left: 1px dashed var(--rule);
  }
  .service-tab { position: absolute; left: -1px; top: 0; width: 168px; height: 56px; }
  .service-title {
    position: absolute; left: 12px; top: 6px; width: 124px;
    color: var(--white); font-weight: 700; font-size: 11.5px; line-height: 1.3;
  }
  .service-title--wide { width: 150px; }
  .service-body {
    position: absolute; left: 8px; top: 58px; width: 152px;
    font-size: 6.9px; line-height: 1.34; color: var(--text);
  }
  .service-lead {
    color: var(--green); font-weight: 400; font-size: 17px; line-height: 1;
  }
  .service-lead .indent { padding-left: 30px; }

  .title-band {
    position: absolute; left: 0; top: 18px; width: 100%; height: 92px;
    background: linear-gradient(180deg, var(--green) 0%, var(--green-dark) 100%);
  }
  .page-title {
    position: absolute; left: 26px; top: 10px; z-index: 2;
    font-weight: 300; font-size: 88px; line-height: 1;
    color: var(--white); letter-spacing: 0;
    white-space: nowrap;
  }
  .feature-photo {
    position: absolute; left: 0; top: 110px; width: 100%; height: 280px;
    background: linear-gradient(180deg, #f2f2f2 0%, #e6e6e6 60%, #cfcfcf 100%);
    z-index: 1;
  }
  .intro {
    position: absolute; left: 38px; top: 432px; width: 500px;
    font-size: 9.6px; line-height: 1.62; color: var(--ink);
  }
  .brand-name {
    position: absolute; right: 40px; top: 5px;
    font-size: 9px; font-weight: 600; color: var(--lime); letter-spacing: .3px;
  }
</style>
</head>
<body>
  <main class="spread">
    <section class="page page--left">
      <div class="top-band"></div>

      <div class="services">
        <article class="service">
          <svg class="service-tab" viewBox="0 0 168 56" aria-hidden="true">
            <polygon points="0,0 168,0 168,34 0,46" fill="var(--green)"/>
            <polygon points="0,46 168,34 168,38 0,52" fill="var(--ink)"/>
          </svg>
          <h2 class="service-title">Marketing Strategy Services</h2>
          <p class="service-body"><span class="service-lead"><span class="indent">Today, more</span><br>than ever,</span> companies need to develop marketing strategies that ensure their capabilities are matched to the market environment in which they operate in order to achieve their overall business objectives. A company’s marketing strategy should be set in the context of the overall corporate strategy. Our consultants work with managers and business owners across all industries to craft solid marketing strategies that help their organizations achieve their overall business purpose.</p>
        </article>

        <article class="service">
          <svg class="service-tab" viewBox="0 0 168 56" aria-hidden="true">
            <polygon points="0,0 168,0 168,34 0,46" fill="var(--green)"/>
            <polygon points="0,46 168,34 168,38 0,52" fill="var(--ink)"/>
          </svg>
          <h2 class="service-title">Pricing Strategy Services</h2>
          <p class="service-body"><span class="service-lead"><span class="indent">Pricing is often</span><br>considered</span> more of an art than a science. It is THE one element of the marketing mix that has the highest potential to turn off the consumers and throw off the competitors. Unfortunately, few companies handle pricing well enough to manage their markets effectively. In competitive markets and during tough times, price management becomes even more critical. Consumers demand lower prices and the threat of price wars pose new challenges for companies.</p>
        </article>

        <article class="service">
          <svg class="service-tab" viewBox="0 0 168 56" aria-hidden="true">
            <polygon points="0,0 168,0 168,34 0,46" fill="var(--green)"/>
            <polygon points="0,46 168,34 168,38 0,52" fill="var(--ink)"/>
          </svg>
          <h2 class="service-title service-title--wide">Brand Strategy Services</h2>
          <p class="service-body"><span class="service-lead"><span class="indent">Having a</span><br>strong brand is<br>important,</span> whether the economy is in trouble or prosperous. But in today’s difficult and competitive market, the benefits of a strong brand are especially significant because they give businesses a critically important competitive edge. Beyond just a memorable logo, a powerful branding creates value for the company, provides employees with direction and motivation, and is a big plus in acquiring new customers.</p>
        </article>

        <article class="service">
          <svg class="service-tab" viewBox="0 0 168 56" aria-hidden="true">
            <polygon points="0,0 168,0 168,34 0,46" fill="var(--green)"/>
            <polygon points="0,46 168,34 168,38 0,52" fill="var(--ink)"/>
          </svg>
          <h2 class="service-title service-title--wide">Go-To-Market Strategy Services</h2>
          <p class="service-body"><span class="service-lead"><span class="indent">Go-to-market</span><br>strategies are all<br>about customers.</span><br>They and their buying behaviors are changing all the time. Therefore, the need for constant attention to the go-to market strategy is very important to keeping it fresh. Even so, most companies base their go-to-market decisions on data that is questionable and dated.</p>
        </article>
      </div>

      <footer class="page-footer">
        <span class="site-address">www.talvenbridgeadvisory.ca</span>
      </footer>
    </section>

    <section class="page page--right">
      <div class="top-band"></div>
      <div class="title-band"></div>
      <div class="feature-photo" role="img" aria-label="Photo of a businessman in a dark suit sketching marketing charts, ideas and a city skyline on a white wall"></div>
      <h1 class="page-title">MARKETING</h1>

      <p class="intro">At Talvenbridge Advisory, we know that the financial success of your business depends in large part upon the marketing ability of your company. But good marketing does not happen by accident. It requires a blend of discipline and flexibility, using the right combination of both art and science. The “right combination” entails having the experience, passion, creativity and strategic thinking, which if carefully planned and executed, can the result in a great business success.</p>

      <footer class="page-footer">
        <span class="brand-name">Talvenbridge Advisory</span>
      </footer>
    </section>
  </main>
</body>
</html>
```